Boot Camp Flyer

Outdoor Boot Camp
SAMPLE DESIGNS I LIKE UPLOADED.
Similar to this or be creative !
I need A5 and DL flyer promoting our Boot Camp program, similar to the sample design but include our details. Pink blue green black white yellow and purple colours ok

PRICE: $100
WHEN: Thursdays & Saturdays
Thursday 6pm
Saturday 9am

WHERE: Brindle Paddock

Get results all year round! 5 week boot camp only $100
Join in any time! Register your place now!

Tone Fast Boot Camp
Register now at kestrelmovement@mailbox.example or www.social.example/kestrelmovementnz
Female only. Registration essential. ALL fitness levels welcome.

Conditions
Valid from Mar 22, 2018
Expires 26th Apr, 2018
Register online. Subject to availability. Valid for new clients only. Valid for unlimited sessions per week. Boot Camps run in 5 week blocks. Non-transferable. No refunds unless required by law. No cashback. Not to be used with any other offer.

Could maybe write 5 week tone fast challenge

Target Market(s)

Female 20s-40s

Industry/Entity Type

Fitness

Colors

Designer to choose colors to be used in the design.

Requirements
Must have
• Colour
• Easy to read font
• Picture of females (target market) exercising
Nice to have
• Terms and conditions in small print down bottom.
Should not have
• Too much text

```html
<!DOCTYPE html>
<html lang="en">
<head>
<meta charset="utf-8">
<title>Outdoor Boot Camp Flyer</title>
<link rel="stylesheet" href="https://fonts.googleapis.com/css2?family=Alfa+Slab+One&family=Montserrat:wght@500;600;700;800&display=swap">
<style>
  :root {
    --blue: #22a9e8;
    --blue-deep: #1f6fb8;
    --purple: #6a2d91;
    --pink: #e4197f;
    --yellow: #fff200;
    --gold: #ffe600;
    --black: #111111;
    --white: #ffffff;
    --page: #eeeeee;
  }
  * { margin: 0; padding: 0; box-sizing: border-box; }
  html, body { width: 900px; height: 1200px; overflow: hidden; background: var(--page); }
  .canvas { position: relative; width: 900px; height: 1200px; }
  .flyer {
    position: absolute; left: 37px; top: 13px;
    width: 700px; height: 995px;
    transform: scale(1.18); transform-origin: 0 0;
    background: var(--white); overflow: hidden;
    font-family: "Montserrat", Arial, sans-serif;
  }
  .flyer-art { position: absolute; inset: 0; }
  .brand-badge {
    position: absolute; left: 30px; top: 170px; width: 110px; height: 110px;
    border-radius: 50%; background: var(--white); border: 2px solid #dddddd;
    display: flex; align-items: center; justify-content: center; text-align: center;
    font-weight: 800; font-size: 14px; line-height: 1.15; color: var(--purple);
  }
  .photo-circle { position: absolute; border-radius: 50%; border: 5px solid var(--blue); }
  .photo-kettlebell { left: 395px; top: 258px; width: 164px; height: 164px;
    background: radial-gradient(circle at 50% 40%, #c9b9c6, #6f8a93); }
  .photo-stretch { left: 540px; top: 316px; width: 132px; height: 132px;
    background: radial-gradient(circle at 50% 45%, #d3c5cc, #7d8f77); }
  .headline {
    position: absolute; left: 27px; top: 308px;
    font-family: "Alfa Slab One", Georgia, serif; font-size: 41px; line-height: 47px;
  }
  .headline .line-1 { color: var(--blue-deep); display: block; }
  .headline .line-2 { color: var(--purple); display: block; }
  .price-bar {
    position: absolute; left: 0; top: 413px; width: 412px; height: 36px;
    background: var(--black); border-radius: 0 18px 18px 0;
    color: var(--white); font-weight: 600; font-size: 16px;
    display: flex; align-items: center; padding-left: 28px; gap: 8px;
  }
  .price-bar .price { color: var(--gold); font-weight: 800; font-size: 24px; }
  .schedule {
    position: absolute; left: 27px; top: 457px;
    color: var(--blue); font-weight: 700; font-size: 16px; line-height: 20.5px;
  }
  .schedule .venue { color: var(--purple); margin-top: 7px; }
  .pitch {
    position: absolute; left: 350px; top: 530px;
    color: var(--purple); font-weight: 700; font-size: 14px; line-height: 19px;
  }
  .campaign {
    position: absolute; left: 350px; top: 610px;
    font-family: "Alfa Slab One", Georgia, serif; font-size: 23px; color: var(--pink);
  }
  .register {
    position: absolute; left: 350px; top: 650px;
    color: var(--black); font-weight: 600; font-size: 14px; line-height: 20px;
  }
  .register .label { font-weight: 700; }
  .register .url-tail { color: var(--blue); }
  .photo-yoga { position: absolute; left: 20px; top: 615px; width: 320px; height: 230px; }
  .audience { position: absolute; left: 28px; top: 660px; width: 168px; text-align: center; }
  .audience .title { color: var(--purple); font-weight: 800; font-size: 19px; }
  .audience .pill {
    display: inline-block; margin-top: 4px; background: var(--gold);
    border-radius: 10px; padding: 2px 10px; font-size: 10px; font-weight: 800; color: var(--purple);
  }
  .audience .seal {
    margin: -4px auto 0; width: 128px; height: 60px;
    background: var(--purple); border-radius: 0 0 64px 64px;
    color: var(--gold); font-size: 10px; font-weight: 600; padding-top: 10px;
  }
  .audience .stars { font-size: 13px; letter-spacing: 6px; }
  .social-band {
    position: absolute; left: 0; top: 862px; width: 700px; height: 38px;
    background: var(--black); color: var(--white);
    font-weight: 600; font-size: 20px; text-align: center; line-height: 38px;
  }
  .terms {
    position: absolute; left: 20px; top: 926px; width: 667px; height: 54px;
    border: 1px solid var(--white); border-radius: 8px;
    color: var(--white); font-size: 8.6px; line-height: 12px; padding: 6px 14px 0;
  }
  .terms .terms-title {
    position: absolute; top: -8px; left: 50%; transform: translateX(-50%);
    background: var(--blue); padding: 0 4px; font-weight: 700; font-size: 9.5px;
  }
  .terms .dates span { display: inline-block; width: 180px; }
</style>
</head>
<body>
<div class="canvas">
  <div class="flyer">
    <svg class="flyer-art" viewBox="0 0 700 995" width="700" height="995">
      <defs>
        <linearGradient id="parkShade" x1="0" y1="0" x2="0" y2="1">
          <stop offset="0" stop-color="#3f5f2a" stop-opacity="0.55"/>
          <stop offset="0.5" stop-color="#c8a89a" stop-opacity="0.35"/>
          <stop offset="1" stop-color="#8cc04f" stop-opacity="0.3"/>
        </linearGradient>
      </defs>
      <path role="img" aria-label="Photo of women doing push-ups together on grass in a park"
            d="M0,0 H700 V458 C610,390 470,322 300,302 C150,285 50,230 0,120 Z" fill="#6f9a4c"/>
      <path d="M0,0 H700 V458 C610,390 470,322 300,302 C150,285 50,230 0,120 Z" fill="url(#parkShade)"/>
      <path d="M0,120 C50,230 150,285 300,302 C470,322 610,390 700,458" fill="none" stroke="var(--blue)" stroke-width="12"/>
      <path d="M0,142 C50,248 150,300 300,318 C470,338 610,405 700,475" fill="none" stroke="var(--purple)" stroke-width="10"/>
      <path d="M0,610 C150,562 300,500 450,486 C560,474 640,480 700,488 V995 H0 Z" fill="var(--yellow)"/>
      <path d="M0,630 C120,615 250,660 340,750 C430,815 500,835 580,818 C630,808 670,795 700,785 V995 H0 Z" fill="var(--blue)"/>
      <path d="M0,630 C120,615 250,660 340,750 C430,815 500,835 580,818 C630,808 670,795 700,785" fill="none" stroke="var(--pink)" stroke-width="6"/>
      <path d="M0,640 C120,626 250,670 340,760 C430,825 500,845 580,828 C630,818 670,805 700,795" fill="none" stroke="var(--purple)" stroke-width="6"/>
    </svg>

    <div class="brand-badge">Kestrel<br>Movement</div>

    <div class="photo-circle photo-kettlebell" role="img" aria-label="Photo of women lifting kettlebells"></div>
    <div class="photo-circle photo-stretch" role="img" aria-label="Photo of women stretching outdoors"></div>

    <h1 class="headline"><span class="line-1">OUTDOOR</span><span class="line-2">BOOT CAMP</span></h1>

    <div class="price-bar"><span class="price">$100</span> 5 week boot camp block</div>

    <div class="schedule">
      <p>Thursday &amp; Saturday</p>
      <p>22nd March - 26th April</p>
      <p>Thursday 6pm</p>
      <p>Saturday 9am</p>
      <p class="venue">At &nbsp;Brindle Paddock</p>
    </div>

    <div class="pitch">
      <p>Get results all year round!</p>
      <p>5 week boot camp only $100.</p>
      <p>Join in any time!</p>
      <p>Register your place now!</p>
    </div>

    <h2 class="campaign">Tone Fast Boot Camp</h2>

    <div class="register">
      <p class="label">Register now at</p>
      <p>kestrelmovement@mailbox.example</p>
      <p>or</p>
      <p>www.social.example/<span class="url-tail">kestrelmovementnz</span></p>
    </div>

    <svg class="photo-yoga" viewBox="0 0 320 230" role="img" aria-label="Photo of a woman in a cobra stretch on a yoga mat">
      <ellipse cx="170" cy="205" rx="150" ry="18" fill="#e6eef3"/>
      <ellipse cx="250" cy="130" rx="55" ry="70" fill="#f1dccb" opacity="0.55"/>
    </svg>

    <div class="audience">
      <p class="title">FEMALE ONLY</p>
      <span class="pill">REGISTRATION ESSENTIAL</span>
      <div class="seal">
        <p class="stars">★★★</p>
        <p>ALL fitness levels welcome.</p>
      </div>
    </div>

    <div class="social-band">social.example/kestrelmovementnz</div>

    <div class="terms">
      <span class="terms-title">* Terms and Conditions *</span>
      <p class="dates"><span>Valid from Mar 22, 2018</span>Expires 26th Apr, 2018</p>
      <p>Register online. Subject to availability. Valid for new clients only. Valid for unlimited sessions per week. Boot Camps run in 5 week blocks.</p>
      <p>Non-transferable. No refunds unless required by law. No cashback. Not to be used with any other offer.</p>
    </div>
  </div>
</div>
</body>
</html>
```